Magnetic Business card Design do a service provider

Hi,

The company aim is to provide all service needs under one roof. However, at the moment there is only Accounting, Electrical and IT branches. There will be more services coming onboard in the future.

I already have a logo designed (Company name is already part of the logo), I now need a magnetic business card designed.

The business card will contain the following:

- Company Logo
- Contact#
- E-mail
- enough space to add website URL (for future)
Updates

Project Deadline Extended Reason: HI All,The deadline has been extended due to not having enough time to review an overwhelming number of designs that has been submitted by lots of designers.I will be uploading a draft of designs that i have in mind.Thanks. Added Friday, January 22, 2016

Target Market(s)

Residential, Home-based Businesses, Small and Medium businesses

Industry/Entity Type

Business

Contact Information for Business Card

Contact#: 0491 738 520
E-mail: service@brightlanetrades.net.au

Font styles to use
Decorative
Script

Requirements
Must have
• Round edges
• Some form of logo incorporation as a background

```html
<!DOCTYPE html>
<html lang="en">
<head>
<meta charset="utf-8">
<title>Brightlane Trades – Business Card</title>
<link rel="stylesheet" href="https://fonts.googleapis.com/css2?family=Lato:wght@400;700&display=swap">
<style>
  :root {
    --backdrop: #dcdad8;
    --card-face: #f3f1f0;
    --brand-blue: #0d5597;
    --mark-tint: #c9d3de;
    --contact-text: #ffffff;
    --name-ink: #1e2a3a;
  }
  * { margin: 0; padding: 0; box-sizing: border-box; }
  html, body {
    width: 1200px;
    height: 900px;
    overflow: hidden;
    background: var(--backdrop);
  }
  .canvas {
    position: relative;
    width: 1200px;
    height: 900px;
  }
  .business-card {
    position: absolute;
    left: 420px;
    top: 180px;
    width: 430px;
    height: 413px;
    background: var(--card-face);
    border-radius: 6px;
    box-shadow: 0 6px 24px rgba(0,0,0,0.12);
  }
  .contact-disc {
    position: absolute;
    left: 180px;
    top: 180px;
    width: 414px;
    height: 414px;
    border-radius: 50%;
    background: var(--brand-blue);
    display: flex;
    flex-direction: column;
    align-items: center;
    justify-content: flex-start;
    gap: 6px;
    padding-top: 176px;
    font-family: "Lato", sans-serif;
    color: var(--contact-text);
  }
  .contact-line {
    display: flex;
    align-items: center;
    gap: 5px;
    font-size: 17px;
    line-height: 22px;
    white-space: nowrap;
  }
  .contact-line svg {
    width: 13px;
    height: 13px;
    fill: var(--contact-text);
    flex: none;
  }
  .brand-mark {
    position: absolute;
    left: 640px;
    top: 366px;
    width: 100px;
    height: 100px;
    border-radius: 50%;
    background: var(--mark-tint);
  }
  .company-name {
    position: absolute;
    left: 582px;
    top: 494px;
    width: 240px;
    text-align: center;
    font-family: "Lato", sans-serif;
    font-weight: 700;
    font-size: 29px;
    line-height: 36px;
    color: var(--name-ink);
    white-space: nowrap;
  }
</style>
</head>
<body>
  <main class="canvas">
    <section class="business-card" aria-label="Brightlane Trades business card"></section>

    <div class="contact-disc">
      <p class="contact-line">
        <svg viewBox="0 0 24 24" aria-hidden="true"><path d="M6.6 10.8a15.2 15.2 0 0 0 6.6 6.6l2.2-2.2c.3-.3.7-.4 1-.2 1.1.4 2.3.6 3.6.6.6 0 1 .4 1 1V20c0 .6-.4 1-1 1A17 17 0 0 1 3 4c0-.6.4-1 1-1h3.5c.6 0 1 .4 1 1 0 1.3.2 2.5.6 3.6.1.3 0 .7-.2 1z"/></svg>
        0491 738 520
      </p>
      <p class="contact-line">
        <svg viewBox="0 0 24 24" aria-hidden="true"><path d="M2 5h20v14H2z" fill="#fff"/><path d="M3.5 6.5 12 13l8.5-6.5" fill="none" stroke="#0d5597" stroke-width="1.8"/></svg>
        service@brightlanetrades.net.au
      </p>
      <p class="contact-line">
        <svg viewBox="0 0 24 24" aria-hidden="true"><circle cx="12" cy="12" r="10" fill="none" stroke="#fff" stroke-width="2"/><path d="M2 12h20M12 2c3 3 3 17 0 20M12 2c-3 3-3 17 0 20" fill="none" stroke="#fff" stroke-width="1.6"/></svg>
        www.brightlanetrades.net.au
      </p>
    </div>

    <div class="brand-mark" aria-hidden="true"></div>
    <p class="company-name">Brightlane Trades</p>
  </main>
</body>
</html>
```